Restaurant needs promotional material

We need a design for a "free welcome cocktail on your next visit" flyer. The flyer must have a black background and be contemporary. Our logo is the name of the restaurant which is "Amber Nook" in edwardian script font with italic selected.

There must be a section for terms and conditions, which are:
1 free cocktail for every main course ordered from our evening menu over the value of 9.95€ (not including taxes). The number of free cocktails cannot exceed the number of main courses ordered from your previous visit. This offer is only valid when you present both this flyer and your receipt from your previous visit. This offer does not include ice cream cocktails. This offer cannot be used in conjunction with any other offer or promotion. Limit 1 free cocktail per person. We reserve the right to final interpretation of this offer and can cancel the offer at any time.

A space must also be left where we can write a "valid until" date.

The uploaded photos are a picture of our cocktail menu and the publicity we are currently running, so you can get a feel for your design.

Thanks

Industry/Entity Type

Restaurant

Colors
000000

Requirements
Must have
• Also included in the flyer is the text " Please present this flyer along with your bill from your previous visit upon arrival.
• Pictures of cocktails!

```html
<!DOCTYPE html>
<html lang="en">
<head>
<meta charset="utf-8">
<title>Amber Nook – Free Cocktail Flyer</title>
<link rel="stylesheet" href="https://fonts.googleapis.com/css2?family=Kalam:wght@700&family=Montserrat:wght@400&family=Roboto+Condensed:wght@700&family=Roboto:ital,wght@0,300;0,400;0,700;1,300;1,400;1,700&display=swap">
<style>
  :root {
    --page-bg: #111111;
    --flyer-bg: #050305;
    --magenta: #e04ee6;
    --pink-text: #e979ef;
    --violet-dark: #2a0f2e;
    --white: #ffffff;
    --frame-grey: #4a4a4a;
    --fire: #e8541c;
  }
  * { margin: 0; padding: 0; box-sizing: border-box; }
  html, body {
    width: 1200px; height: 1200px; overflow: hidden;
    background: var(--page-bg);
  }
  .flyer {
    position: absolute; left: 315px; top: 20px;
    width: 570px; height: 1160px;
    background: var(--flyer-bg);
    overflow: hidden;
    font-family: "Roboto", sans-serif;
    color: var(--white);
  }
  .flyer > * { position: absolute; }

  .header-band {
    left: 0; top: 0; width: 570px; height: 74px;
    background: linear-gradient(180deg, #1b1020 0%, #3d1a45 100%);
  }
  .header-label {
    left: 0; top: 44px; width: 570px; text-align: center;
    font-family: "Montserrat", sans-serif; font-size: 22px;
    letter-spacing: 19px; padding-left: 19px; line-height: 1;
  }
  .logo-band {
    left: 0; top: 74px; width: 570px; height: 86px;
    background: linear-gradient(180deg, #b33bbb 0%, var(--magenta) 45%, #a02fa8 100%);
    display: flex; align-items: center; justify-content: center;
  }
  .logo-name {
    font-family: "Kalam", cursive; font-weight: 700;
    font-size: 62px; line-height: 1; color: var(--white);
    padding-top: 8px;
  }
  .offer-zone {
    left: 0; top: 160px; width: 570px; height: 238px;
    background: radial-gradient(ellipse at 70% 45%, #5b2463 0%, var(--violet-dark) 55%, var(--flyer-bg) 100%);
  }
  .address {
    left: 0; top: 164px; width: 570px; text-align: center;
    font-size: 16px; font-weight: 400;
  }
  .cocktail-art {
    left: 60px; top: 203px; width: 92px; height: 186px;
    background: radial-gradient(circle at 50% 22%, #fff3c8 0%, #f0a24a 18%, #b8324a 38%, rgba(90,20,60,0.4) 70%, transparent 100%);
  }
  .offer-headline {
    left: 168px; top: 190px;
    font-family: "Kalam", cursive; font-weight: 700;
    font-size: 64px; line-height: 1; letter-spacing: 2px;
  }
  .offer-headline .num { margin-right: 30px; }
  .offer-sub {
    left: 240px; top: 249px;
    font-family: "Kalam", cursive; font-weight: 700;
    font-size: 38px; line-height: 1; color: var(--magenta);
  }
  .offer-body {
    left: 166px; top: 300px; width: 400px;
    font-size: 22px; font-weight: 300; line-height: 26px; color: var(--pink-text);
  }
  .offer-body .price { color: var(--white); font-weight: 700; font-size: 27px; }
  .offer-body .tax { color: var(--white); font-style: italic; font-size: 13px; }

  .grill-art {
    left: 311px; top: 385px; width: 259px; height: 255px;
    background: radial-gradient(ellipse at 70% 40%, #f7a33a 0%, var(--fire) 28%, #6a1a0c 58%, transparent 80%);
  }
  .rule-note {
    left: 26px; top: 410px; width: 300px; height: 102px;
    border-left: 6px solid var(--magenta);
    padding-left: 12px;
    font-size: 22px; font-weight: 300; line-height: 26px; color: var(--pink-text);
  }
  .terms-box {
    left: 26px; top: 533px; width: 512px; height: 258px;
    border: 1px solid var(--frame-grey);
  }
  .terms-lead {
    left: 43px; top: 546px; width: 268px;
    font-size: 22px; font-weight: 300; line-height: 26px; color: var(--pink-text);
  }
  .terms-fine {
    left: 43px; top: 678px; width: 490px;
    font-style: italic; color: var(--pink-text);
  }
  .terms-fine .first { font-size: 18px; line-height: 24px; display: block; }
  .terms-fine .small { font-size: 14.5px; line-height: 26px; font-weight: 300; display: block; }
  .terms-fine strong { font-weight: 700; }

  .logo-band-small {
    left: 57px; top: 813px; width: 326px; height: 48px;
    background: linear-gradient(180deg, #b33bbb 0%, var(--magenta) 50%, #a02fa8 100%);
    display: flex; align-items: center; justify-content: center;
  }
  .logo-band-small .logo-name { font-size: 36px; padding-top: 6px; }
  .storefront-art {
    left: 0; top: 861px; width: 570px; height: 164px;
    background: linear-gradient(180deg, #3b1d5e 0%, #c22a78 35%, #e0557e 60%, #3a1030 100%);
  }
  .arrival-note {
    left: 26px; top: 1031px; width: 520px;
    font-size: 14px; font-style: italic; font-weight: 400; color: var(--pink-text);
  }
  .valid-until {
    left: 26px; top: 1058px; font-size: 18px; font-style: italic; font-weight: 300;
  }
  .reservations {
    left: 26px; top: 1086px;
    font-family: "Roboto Condensed", sans-serif; font-weight: 700; font-size: 26px;
  }
  .website {
    left: 26px; top: 1124px; font-size: 20px; letter-spacing: 2px; font-weight: 400;
  }
  .wifi-note {
    left: 400px; top: 1084px; width: 142px; text-align: center;
    font-size: 30px; font-weight: 700; line-height: 34px;
  }
  .wifi-note .top { font-size: 18px; display: block; line-height: 22px; }
  .bottom-glow {
    left: 40px; top: 1155px; width: 490px; height: 2px;
    background: linear-gradient(90deg, transparent, #f3c38a, transparent);
  }
</style>
</head>
<body>
  <div class="flyer">
    <div class="header-band"></div>
    <div class="header-label">RESTAURANT</div>
    <div class="logo-band"><span class="logo-name">Amber Nook</span></div>

    <div class="offer-zone"></div>
    <div class="address">Paseo Marina Azul, C.C. Brisamar, Playa del Faro Costa Dorada</div>
    <div class="cocktail-art" role="img" aria-label="Illustration of a glowing martini cocktail with a cherry"></div>
    <div class="offer-headline"><span class="num">1</span>FREE</div>
    <div class="offer-sub">cocktail</div>
    <div class="offer-body">for every main course ordered<br>from our evening menu over the<br>value of <span class="price">9.95€</span> <span class="tax">(not including taxes).</span></div>

    <div class="grill-art" role="img" aria-label="Photo of grilled meat over flames with a flyer and receipt silhouette"></div>
    <div class="rule-note">The number of free cocktails cannot exceed the number of main courses ordered from your previous visit</div>

    <div class="terms-box"></div>
    <div class="terms-lead">This offer is only valid when you present both this flyer and your receipt from your previous visit.</div>
    <div class="terms-fine">
      <span class="first">*This offer does not include ice cream cocktails.</span>
      <span class="small">This offer cannot be used in conjunction with any other offer or<br>promotion. Limit <strong>1 free cocktail per person.</strong> We reserve the right to<br>final interpretation of this offer and can cancel the offer at any time.</span>
    </div>

    <div class="logo-band-small"><span class="logo-name">Amber Nook</span></div>
    <div class="storefront-art" role="img" aria-label="Photo of the restaurant terrace at night with pink lights and palm plants"></div>

    <div class="arrival-note">Please present this flyer along with your bill from your previous visit upon arrival.</div>
    <div class="valid-until">valid until" date :</div>
    <div class="reservations">FOR RESERVATIONS - 922 41 58 03</div>
    <div class="website">www.ambernook-dining.com</div>
    <div class="wifi-note"><span class="top">FREE</span>WIFI</div>
    <div class="bottom-glow"></div>
  </div>
</body>
</html>
```